Packaged Food Business Needs a Packaging Design

We need a package design to be used as a label/sticker on the lids of round and square transparent plastic containers and on the sides of resealable stand-up pouches. The brand name is 'Tastora' - please find attached logo together with pictures of the sample containers and pouch. We will use the packaging to market a wide variety of food categories from nuts, dried fruits, spices, cooking chocolates, baking ingredients, cereals, grains and pulses.

OVERALL FEEDBACK ON DESIGNS ALREADY RECEIVED:

- We have found so far that a lot of our mandatory requirements are not adhered to in designs that have been submitted so far. We would like to emphasise that the ingredient, weight and expiry text will be printed at the time of packing so it should not take prime space on the pack BUT at the same time some 'blank' space needs to flawlessly be incorporated into the overall design for this purpose
- We encourage you to glorify the brand logo in the pack, and absolutely refrain from duplicating the tagline
- Please note that ONE label design will be used to pack a wide variety of food ingredients and therefore please ensure that the choice of your design incorporates this requirement, in the past we have received designs that are limited to only one type of food (like nuts) or have received designs that are too floral or leafy (and not grounded to food
- Please ensure that you submit designs for all three packaging formats, it is critical to see the family look from the on-set

Target Market(s)

The brand is targeting both mothers and professional chefs and therefore the label design should be broadly approachable and convey affordable premium

Industry/Entity Type

Business

Requirements
Must have
• - Consistent with the brand name and logo, the overall look and feel of the packaging should convey values of healthy, gourmet food ingredients, high in nourishment and project a sense of delightful taste
• - The design styling to be modern and 'simplistic' (embracing 'less-is-more' type of a design style)
• - Design a packaging architecture that incorporates the brand logo together with its tagline lock-up of 'savour the goodness in every morsel' - find logo attached
• - The design needs to have a dedicated area to print the ingredient (e.g., Mixed Nuts), weight (e.g., 500g) and expiry (this space needs to be flawlessly incorporated into the design) - this information will be printed either with an inkjet printer or with a rubber stamp so please leave an empty space (the text should not be part of the design, just the area for the text needs to be included in the design)
• - The packaging must include 'Packed By: Kelvane Distributors Ltd, P. O. Box 51946, Kampala - Uganda'
• - For the design of the resealable pouch, please incorporate a window to see through the ingredients and a hole on top to hang on supermarket pegs if necessary
Nice to have
• - We would love to have some design submissions that are bold and cheerful and fun (but not frivolous) - please see attached inspiration for 'fun' packaging. The attachments are purely for inspiration, not to infringe on anyone else's TM and copyrights
• - Incorporate green to convey healthy, organic values
• - Explore use of gold and silver convey premiumness
Should not have
• - Do not duplicate the tagline
• - Do not include the ingredient, weight and expiry in the main graphic of the design, these will be printed at the time of packing so ensure there is provision for this in a flawless way in the design (e.g., via a blank space allocated for this purpose)

```html
<!DOCTYPE html>
<html lang="en">
<head>
<meta charset="utf-8">
<title>Tastora Packaging Labels</title>
<link rel="stylesheet" href="https://fonts.googleapis.com/css2?family=Source+Sans+3:wght@400;800&display=swap">
<style>
  :root {
    --sky: #1fa3dc;
    --sky-light: #5cc4ee;
    --hill-dark: #2d6b2a;
    --grass: #6dbb3c;
    --grass-light: #8ccf4a;
    --brand-brown: #4a2412;
    --tag-green: #3f8f2a;
    --label-white: #ffffff;
    --page: #ffffff;
    --text-dark: #2a2a2a;
    --product: #b9823e;
    --product-dark: #7a4c20;
  }
  * { box-sizing: border-box; margin: 0; padding: 0; }
  html, body { width: 1200px; height: 1200px; overflow: hidden; background: var(--page); }
  body { position: relative; font-family: "Source Sans 3", sans-serif; }

  .label { position: absolute; overflow: hidden; }
  .scene-art {
    position: absolute; inset: 0;
    background: linear-gradient(180deg, var(--sky) 0%, var(--sky-light) 30%, var(--hill-dark) 42%, var(--grass) 62%, var(--grass-light) 100%);
  }
  .brand { position: absolute; left: 0; right: 0; text-align: center; }
  .brand-name {
    font-weight: 800; color: var(--brand-brown); letter-spacing: 0.06em;
    text-transform: uppercase; line-height: 1;
  }
  .brand-mark {
    display: inline-block; border-radius: 50%; background: var(--label-white);
    vertical-align: middle; margin-right: 10px;
  }
  .tagline {
    font-weight: 800; color: var(--tag-green); text-transform: uppercase;
    letter-spacing: 0.04em; background: var(--label-white);
    display: inline-block; padding: 2px 8px; border-radius: 4px; margin-top: 6px;
  }
  .print-area { position: absolute; background: var(--label-white); }
  .packed-by { position: absolute; left: 0; right: 0; text-align: center; color: var(--text-dark); }

  /* Lid label */
  .lid { left: 110px; top: 110px; width: 400px; height: 400px; border-radius: 50%; }
  .lid .brand { top: 150px; }
  .lid .brand-name { font-size: 56px; }
  .lid .brand-mark { width: 22px; height: 22px; }
  .lid .tagline { font-size: 12px; }

  /* Tub wrap label */
  .tub-wrap { left: 60px; top: 620px; width: 500px; height: 380px; border-radius: 8px; }
  .tub-wrap .brand { top: 70px; }
  .tub-wrap .brand-name { font-size: 64px; }
  .tub-wrap .brand-mark { width: 24px; height: 24px; }
  .tub-wrap .tagline { font-size: 13px; }
  .tub-wrap .print-area { left: 70px; right: 70px; top: 200px; height: 110px; border-radius: 6px; }
  .tub-wrap .packed-by { top: 330px; font-size: 14px; }

  /* Pouch label */
  .pouch { left: 640px; top: 160px; width: 500px; height: 680px; border-radius: 14px; }
  .pouch .brand { top: 90px; padding-left: 90px; }
  .pouch .brand-name { font-size: 64px; }
  .pouch .brand-mark { width: 24px; height: 24px; }
  .pouch .tagline { font-size: 13px; }
  .pouch .window {
    position: absolute; left: 145px; top: 235px; width: 220px; height: 250px;
    border-radius: 40px; border: 4px solid var(--label-white);
    background: radial-gradient(circle at 45% 40%, var(--product) 0%, var(--product-dark) 100%);
  }
  .pouch .print-area { left: 70px; right: 70px; top: 515px; height: 110px; }
  .pouch .packed-by { top: 645px; font-size: 14px; }
</style>
</head>
<body>

  <section class="label lid" aria-label="Lid label">
    <div class="scene-art" role="img" aria-label="Illustrated orchard scene with sun, sky, green hills and fruit trees"></div>
    <div class="brand">
      <div class="brand-name"><span class="brand-mark"></span>Tastora</div>
      <div class="tagline">Savour the goodness in every morsel</div>
    </div>
  </section>

  <section class="label tub-wrap" aria-label="Tub side label">
    <div class="scene-art" role="img" aria-label="Illustrated orchard scene with fruit trees on green hills under a blue sky"></div>
    <div class="brand">
      <div class="brand-name"><span class="brand-mark"></span>Tastora</div>
      <div class="tagline">Savour the goodness in every morsel</div>
    </div>
    <div class="print-area" aria-label="Blank area for ingredient, weight and expiry"></div>
    <p class="packed-by">Packed By: Kelvane Distributors Ltd, P. O. Box 51946, Kampala - Uganda</p>
  </section>

  <section class="label pouch" aria-label="Pouch front label">
    <div class="scene-art" role="img" aria-label="Illustrated scene with bright sun, blue sky, green hills and fruit trees"></div>
    <div class="brand">
      <div class="brand-name"><span class="brand-mark"></span>Tastora</div>
      <div class="tagline">Savour the goodness in every morsel</div>
    </div>
    <div class="window" role="img" aria-label="See-through window showing the packed food product"></div>
    <div class="print-area" aria-label="Blank area for ingredient, weight and expiry"></div>
    <p class="packed-by">Packed By: Kelvane Distributors Ltd, P. O. Box 51946, Kampala - Uganda</p>
  </section>

</body>
</html>
```